Harborline Crest Insurance Services

we are a high end insurance agency we specialize on Auto | Home | Business | Life looking for something professional and luxuries at the same time. if you guys need anything else please let me know.

Auto | Home | Business | Life must be under logo on the back with black background.

i want the back part to be black with our gold logo on it.

Target Market(s)

Auto | Home | Business | Life

Industry/Entity Type

Insurance Broker

Contact Information for Business Card

My logo is gold so a black in the back would be nice.

Font styles to use
Serif

Colors
000000

Requirements
Must have
• Big logo on the back with black background.

```html
<!DOCTYPE html>
<html lang="en">
<head>
<meta charset="utf-8">
<title>Harborline Crest Insurance Services – Business Card</title>
<link rel="stylesheet" href="https://fonts.googleapis.com/css2?family=Great+Vibes&family=Cinzel:wght@600&family=Cormorant+Garamond:ital,wght@1,500;1,600&family=Montserrat:wght@500;600&display=swap">
<style>
  :root {
    --stage: #939497;
    --sky-light: #f4f8fc;
    --sky-mid: #b9cfe8;
    --sky-deep: #2f5a98;
    --name-blue: #1f5b9a;
    --ink: #1a1a1a;
    --broker-red: #a8262b;
    --rule-gold: #b08a4a;
    --photo-warm: #d9a987;
    --photo-light: #eedccd;
    --night: #05070d;
    --night-blue: #141c33;
    --gold: #e5b834;
    --white: #ffffff;
  }
  * { margin: 0; padding: 0; box-sizing: border-box; }
  html, body { width: 1200px; height: 1200px; overflow: hidden; }
  body { background: var(--stage); position: relative; }

  .card { position: absolute; left: 180px; width: 840px; height: 478px; overflow: hidden; }

  /* Front */
  .card-front { top: 120px; background: var(--sky-light); }
  .front-backdrop {
    position: absolute; inset: 0;
    background:
      radial-gradient(ellipse at 45% 35%, var(--sky-light) 0%, rgba(244,248,252,0.6) 35%, transparent 70%),
      linear-gradient(120deg, var(--sky-deep) 0%, var(--sky-mid) 28%, var(--sky-light) 55%, var(--sky-mid) 100%);
  }
  .portrait {
    position: absolute; left: 492px; top: 0; width: 348px; height: 100%;
    background: radial-gradient(ellipse at 45% 40%, var(--photo-light) 0%, var(--photo-warm) 60%, #c98f6d 100%);
  }
  .inner-frame { position: absolute; inset: 8px; border: 1px solid rgba(255,255,255,0.85); pointer-events: none; }

  .agent-name {
    position: absolute; left: 52px; top: 130px;
    font-family: "Great Vibes", cursive; font-size: 92px; line-height: 1;
    color: var(--name-blue); white-space: nowrap;
  }
  .tag-line {
    position: absolute; left: 140px; top: 222px;
    font-family: "Cormorant Garamond", serif; font-style: italic; font-weight: 600;
    font-size: 36px; letter-spacing: 5px; color: var(--ink); white-space: nowrap;
  }
  .job-title {
    position: absolute; left: 116px; top: 358px;
    font-family: "Montserrat", sans-serif; font-weight: 500; font-size: 27px;
    color: var(--broker-red); white-space: nowrap;
  }
  .title-rule { position: absolute; left: 112px; top: 390px; width: 312px; height: 1px; background: var(--rule-gold); }
  .contact-line {
    position: absolute; left: 70px; top: 396px; display: flex; align-items: center; gap: 6px;
    font-family: "Montserrat", sans-serif; font-weight: 600; font-size: 21px; color: var(--ink); white-space: nowrap;
  }
  .contact-line svg { width: 18px; height: 18px; flex: none; }
  .contact-line .gap { width: 4px; }
  .pic-note {
    position: absolute; left: 580px; top: 402px;
    font-family: "Cormorant Garamond", serif; font-style: italic; font-weight: 500;
    font-size: 24px; color: var(--ink); white-space: nowrap;
  }

  /* Back */
  .card-back { top: 654px; height: 480px; background: var(--night); }
  .back-backdrop {
    position: absolute; inset: 0;
    background:
      radial-gradient(ellipse at 70% 20%, rgba(40,55,90,0.55) 0%, transparent 55%),
      linear-gradient(160deg, var(--night-blue) 0%, var(--night) 55%, #0a1020 100%);
  }
  .brand-mark {
    position: absolute; left: 104px; top: 154px; width: 160px; height: 160px;
    border-radius: 50%; background: var(--gold);
  }
  .brand-name {
    position: absolute; left: 316px; top: 188px;
    font-family: "Cinzel", serif; font-weight: 600; font-size: 36px; line-height: 1.15;
    color: var(--gold); white-space: nowrap;
  }
  .service-lines {
    position: absolute; left: 310px; top: 296px;
    font-family: "Montserrat", sans-serif; font-weight: 600; font-size: 29px;
    color: var(--white); white-space: nowrap; letter-spacing: 0.5px;
  }
</style>
</head>
<body>
  <section class="card card-front">
    <div class="front-backdrop" role="img" aria-label="Photo of skyscrapers rising into a bright blue sky with clouds"></div>
    <div class="portrait" role="img" aria-label="Portrait photo of the insurance broker"></div>
    <div class="inner-frame"></div>

    <h1 class="agent-name">Marcus Ellery</h1>
    <p class="tag-line">Your Tag Line</p>
    <p class="job-title">INSURANCE BROKER</p>
    <div class="title-rule"></div>
    <p class="contact-line">
      <svg viewBox="0 0 24 24" aria-hidden="true"><path fill="#a8262b" d="M6.6 2.5c.6-.3 1.3 0 1.6.6l1.6 3.5c.3.6.1 1.2-.4 1.6L8 9.3c.9 2.5 3.2 5 5.7 6.3l1.2-1.3c.4-.5 1.1-.6 1.6-.3l3.3 1.9c.6.3.8 1 .5 1.6l-1 2.2c-.4.9-1.4 1.4-2.4 1.2C10 19.6 4.2 13.5 3.2 6.5c-.1-1 .4-1.9 1.3-2.4z"/></svg>
      <span>123.456.7890</span>
      <span class="gap"></span>
      <svg viewBox="0 0 24 24" aria-hidden="true"><g fill="none" stroke="#a8262b" stroke-width="2"><circle cx="12" cy="12" r="9.5"/><ellipse cx="12" cy="12" rx="4.2" ry="9.5"/><path d="M2.5 12h19M4 7h16M4 17h16"/></g></svg>
      <span>www.urwebsite.com</span>
    </p>
    <p class="pic-note">Your Pic goes here</p>
  </section>

  <section class="card card-back">
    <div class="back-backdrop" role="img" aria-label="Dark photo of skyscrapers seen from below at night"></div>
    <div class="brand-mark"></div>
    <p class="brand-name">HARBORLINE CREST<br>INSURANCE SERVICES</p>
    <p class="service-lines">AUTO | HOME | BUSINESS | LIFE</p>
  </section>
</body>
</html>
```